Regal Sweepers Brochure

Please see Attached is a Old Brochure of another company we owe, We need something like this with Regal Sweepers Logos and info
Lots of colors and picture of houses and family

Regal Sweepers
318 Corvel Avenue
Suite 17
Saint Paul, MN 55990
info@regalsweepers.example
612-555-0143

Regal Sweepers
318 Corvel Avenue
Suite 17
Saint Paul, MN 55990
info@regalsweepers.example
612-555-0143

Target Market(s)

Home Owners

Industry/Entity Type

It Company

Font styles to use
Serif

Requirements
Must have
• House picture Family picture lots pictures, Inside house pictures
Nice to have
• Please see Attached is a Old Brochure of another company we owe, We need something like this with Regal Sweepers Logos and info
• Lots of colors and picture of houses and family
• Regal Sweepers
• 318 Corvel Avenue
• Suite 17
• Saint Paul, MN 55990
• info@regalsweepers.example
• 612-555-0143

```html
<!DOCTYPE html>
<html lang="en">
<head>
<meta charset="utf-8">
<title>Regal Sweepers Brochure</title>
<link href="https://fonts.googleapis.com/css2?family=Raleway:wght@400;500;600;700&family=Oswald:wght@400;500&family=Lobster&family=Arimo:ital,wght@0,400;0,700;1,700&display=swap" rel="stylesheet">
<style>
  :root {
    --backdrop: #e4e4e4;
    --paper: #ffffff;
    --brand-blue: #1e8fd3;
    --sky-blue: #5cc4ef;
    --sun-yellow: #f7c12a;
    --bullet-yellow: #f5c518;
    --address-violet: #6b6ec2;
    --ink: #1a1a1a;
  }
  * { margin: 0; padding: 0; box-sizing: border-box; }
  html, body { width: 1200px; height: 896px; overflow: hidden; background: var(--backdrop); }
  .brochure {
    position: absolute; left: 87px; top: 45px; width: 1019px; height: 792px;
    background: var(--paper); box-shadow: 0 1px 3px rgba(0,0,0,.35); overflow: hidden;
  }
  .services-panel { position: absolute; left: 0; top: 0; width: 340px; height: 792px; font-family: "Arimo", Arial, sans-serif; color: var(--ink); }
  .corner-swoosh { position: absolute; left: 0; top: 0; }
  .services-intro { position: absolute; left: 33px; top: 40px; width: 300px; font-size: 13.5px; font-weight: 700; font-style: italic; line-height: 17px; }
  .service-list { position: absolute; left: 33px; top: 106px; font-size: 12.6px; line-height: 15.27px; }
  .service-list h3 { font-size: 12.6px; font-weight: 700; }
  .service-list ul { list-style: none; }
  .service-list li { padding-left: 14px; position: relative; }
  .service-list li::before { content: ""; position: absolute; left: 5px; top: 5px; width: 5px; height: 5px; border-radius: 50%; background: var(--bullet-yellow); }
  .promise { position: absolute; left: 31px; top: 694px; font-family: "Lobster", cursive; font-size: 17.5px; line-height: 23px; color: var(--ink); }

  .web-band { position: absolute; left: 340px; top: 0; width: 679px; height: 57px; background: var(--brand-blue); }
  .web-address { position: absolute; top: 22px; font-family: "Raleway", sans-serif; font-weight: 700; font-size: 17px; color: #fff; text-align: center; width: 336px; }
  .web-address.middle { left: 0; }
  .web-address.right { left: 336px; width: 343px; }

  .contact-block { position: absolute; left: 340px; top: 154px; width: 336px; text-align: center; font-family: "Oswald", sans-serif; font-size: 20.5px; line-height: 27.6px; color: var(--address-violet); }
  .contact-block .company { color: var(--sun-yellow); font-weight: 500; }

  .family-photo { position: absolute; left: 676px; top: 57px; width: 343px; height: 316px; background: linear-gradient(160deg, #dfe6ee 0%, #f3f1ea 45%, #c9b79d 100%); }
  .brand-plate { position: absolute; left: 722px; top: 401px; width: 244px; height: 94px; display: flex; align-items: center; justify-content: center; gap: 10px; }
  .brand-plate .dot { width: 22px; height: 22px; border-radius: 50%; background: var(--sun-yellow); }
  .brand-plate .name { font-family: "Raleway", sans-serif; font-weight: 700; font-size: 26px; color: #222; }

  .wave { position: absolute; left: 340px; top: 480px; }
  .photo-circle { position: absolute; border-radius: 50%; border: 3px solid var(--sun-yellow); }
  .photo-circle.house { left: 397px; top: 408px; width: 122px; height: 122px; background: linear-gradient(180deg, #cfe3ef, #7c8a92 70%, #5f7a4a); }
  .photo-circle.cleaner { left: 480px; top: 427px; width: 152px; height: 152px; background: linear-gradient(150deg, #e9eef2, #c8d4de 60%, #9fb2c0); }
  .photo-circle.supplies { left: 361px; top: 517px; width: 234px; height: 234px; background: radial-gradient(circle at 50% 55%, #f5d24a 0%, #e58ab0 35%, #ffffff 75%); }

  .tagline { position: absolute; left: 676px; top: 554px; width: 343px; text-align: center; font-family: "Raleway", sans-serif; color: #fff; }
  .tagline h2 { font-size: 19.5px; font-weight: 700; line-height: 24px; color: var(--sun-yellow); }
  .tagline h4 { margin-top: 2px; font-size: 13px; font-weight: 600; letter-spacing: .2px; }
  .tagline blockquote { margin: 10px auto 0; width: 290px; font-size: 15px; line-height: 20.4px; font-weight: 500; }
</style>
</head>
<body>
<main class="brochure">
  <section class="services-panel">
    <svg class="corner-swoosh" width="180" height="170" viewBox="0 0 180 170" aria-hidden="true">
      <path d="M0 0 H180 C120 40 60 100 30 170 H0 Z" fill="#12b6ea"/>
    </svg>
    <p class="services-intro">We provide these cleaning and housekeeping services every time we’re in your home:</p>
    <div class="service-list">
      <h3>Bathrooms and Utility:</h3>
      <ul>
        <li>Tile walls</li><li>Bathtubs and showers cleaned</li><li>Shower doors cleaned</li><li>Vanity and sink cleaned</li><li>Mirrors and chrome fixtures cleaned and shined</li><li>Floors cleaned/carpets vacuumed</li><li>Toilets thoroughly cleaned</li><li>Window sills and ledges dusted</li><li>Cobwebs removed</li><li>Doors and door frames spot cleaned</li><li>General dusting</li>
      </ul>
      <h3>Kitchen and Eating Areas:</h3>
      <ul>
        <li>Eating Areas and Counter tops cleaned</li><li>Outside of range hood cleaned</li><li>Top and front of range cleaned</li><li>Drip pans or glass top surfaces wiped</li><li>Sinks cleaned and chrome shined</li><li>Fronts of all appliances cleaned</li><li>Floors vacuumed and damp mopped</li><li>Window sills and ledges dusted</li><li>Cobwebs removed</li><li>Microwave wiped out</li><li>Doors and door frames spot cleaned</li><li>General dusting</li>
      </ul>
      <h3>Sleeping and Living Areas:</h3>
      <ul>
        <li>Flat areas hand wiped</li><li>Doors and door frames spot cleaned</li><li>Cobwebs removed</li><li>Picture frames dusted</li><li>Ceiling fans dusted</li><li>Lamp shades dusted</li><li>Intricate items dusted</li><li>Heavy knickknack areas dusted</li><li>Window sills and ledges dusted</li><li>Wood floors vacuumed and damp mopped</li><li>Stairs vacuumed</li><li>Empty closet floors vacuumed</li>
      </ul>
    </div>
    <p class="promise">All readily accessible floors vacuumed.<br>Bonded and Insured.</p>
  </section>

  <header class="web-band">
    <span class="web-address middle">regalsweepers.example</span>
    <span class="web-address right">regalsweepers.example</span>
  </header>

  <address class="contact-block">
    <div class="company">REGAL SWEEPERS</div>
    <div>318 Corvel Avenue</div>
    <div>Suite 17</div>
    <div>Saint Paul, MN 55990</div>
    <div>info@regalsweepers.example</div>
    <div>612-555-0143</div>
  </address>

  <div class="family-photo" role="img" aria-label="Smiling family of four standing in front of a white two-storey house"></div>

  <div class="brand-plate"><span class="dot"></span><span class="name">Regal Sweepers</span></div>

  <svg class="wave" width="679" height="312" viewBox="0 0 679 312" aria-hidden="true">
    <path d="M0 48 C80 80 180 86 290 68 C420 46 560 26 679 32 V312 H0 Z" fill="var(--sky-blue)"/>
    <path d="M0 68 C90 96 190 98 300 80 C440 58 570 46 679 60 V312 H0 Z" fill="var(--brand-blue)"/>
  </svg>

  <div class="photo-circle house" role="img" aria-label="Suburban house with trees"></div>
  <div class="photo-circle cleaner" role="img" aria-label="Cleaner wiping a window indoors"></div>
  <div class="photo-circle supplies" role="img" aria-label="Basket of cleaning bottles, cloths and gloves"></div>

  <section class="tagline">
    <h2>Professional, Reliable,<br>Trustworthy</h2>
    <h4>CLEANING AND HOUSEKEEPING SERVICES</h4>
    <blockquote>“We created Regal Sweepers with people like you in mind. Our goal is to be the best service company in each area we service. Our commitment to each customer shines brightly in our company’s workforce.”</blockquote>
  </section>
</main>
</body>
</html>
```